Quillory Nest Business Card

I need a business card design. We are a collaborate online training company. Our colors are gray and green. Our website is QuilloryNest.com

I would like an area for a profile picture within the card

```html
<!DOCTYPE html>
<html lang="en">
<head>
<meta charset="utf-8">
<title>Quillory Nest Business Card</title>
<link rel="stylesheet" href="https://fonts.googleapis.com/css2?family=PT+Sans:wght@400;700&display=swap">
<style>
  :root {
    --page: #e9e7e2;
    --card-white: #ffffff;
    --card-black: #0b0b0b;
    --ink: #1a1a1a;
    --green: #7dc242;
    --photo: #cfd3cc;
  }
  * { margin: 0; padding: 0; box-sizing: border-box; }
  html, body { width: 1200px; height: 900px; overflow: hidden; }
  body {
    background: var(--page);
    font-family: "PT Sans", Arial, sans-serif;
    position: relative;
  }
  .card {
    position: absolute;
    top: 302px;
    width: 520px;
    height: 297px;
    overflow: hidden;
    box-shadow: 0 8px 22px rgba(0,0,0,.22);
  }
  .card-front { left: 60px; background: var(--card-white); }
  .card-back  { left: 620px; background: var(--card-black); }

  .front-wave { position: absolute; inset: 0; width: 520px; height: 297px; }

  .brand {
    position: absolute;
    display: flex;
    align-items: center;
    gap: 8px;
    font-weight: 700;
    letter-spacing: -0.5px;
    white-space: nowrap;
    line-height: 1;
  }
  .brand-dot { border-radius: 50%; background: var(--green); flex: none; }
  .brand-front { top: 28px; right: 26px; font-size: 28px; color: var(--ink); }
  .brand-front .brand-dot { width: 20px; height: 20px; }

  .profile-photo {
    position: absolute;
    left: 34px;
    top: 22px;
    width: 76px;
    height: 76px;
    border-radius: 50%;
    background: radial-gradient(circle at 40% 35%, #e3e6e0, var(--photo));
    border: 3px solid var(--green);
  }

  .person { position: absolute; left: 34px; top: 112px; }
  .person-name { font-size: 22px; font-weight: 700; color: var(--ink); line-height: 1; }
  .person-name .surname { color: var(--green); }
  .person-role { font-size: 15px; color: var(--ink); margin-top: 4px; line-height: 1; }

  .contact {
    position: absolute;
    left: 262px;
    top: 200px;
    color: var(--card-white);
    font-size: 12px;
    line-height: 14.5px;
    list-style: none;
    white-space: nowrap;
  }
  .contact li { display: flex; align-items: center; gap: 6px; }
  .contact .icon { width: 11px; height: 11px; flex: none; }

  .brand-back {
    top: 126px;
    left: 150px;
    font-size: 36px;
    color: var(--card-white);
  }
  .brand-back .brand-dot { width: 26px; height: 26px; }
  .back-url {
    position: absolute;
    top: 172px;
    left: 150px;
    font-size: 13px;
    color: var(--green);
  }
</style>
</head>
<body>
  <section class="card card-front">
    <svg class="front-wave" viewBox="0 0 520 297" aria-hidden="true">
      <path d="M0,297 L0,232 C150,215 260,200 340,165 C410,135 465,118 520,112 L520,297 Z" fill="#0b0b0b"/>
      <path d="M0,216 C150,199 260,184 340,149 C410,119 465,102 520,96" fill="none" stroke="#0b0b0b" stroke-width="8"/>
      <path d="M90,216 C190,200 270,188 345,156 C412,127 466,110 520,104" fill="none" stroke="#7dc242" stroke-width="2.5"/>
      <path d="M230,170 C290,158 320,148 350,134 C415,105 468,88 520,82" fill="none" stroke="#7dc242" stroke-width="3"/>
      <path d="M330,128 C400,100 460,82 520,74" fill="none" stroke="#7dc242" stroke-width="6"/>
    </svg>

    <div class="profile-photo" role="img" aria-label="Profile photo of the card holder"></div>

    <div class="brand brand-front"><span class="brand-dot"></span>Quillory Nest</div>

    <div class="person">
      <p class="person-name">Reed <span class="surname">Calloway</span></p>
      <p class="person-role">Founder</p>
    </div>

    <ul class="contact">
      <li>Quillory Nest</li>
      <li>418 W Marlow Ave. Suite 7</li>
      <li>Fenwick, Arizona 85310</li>
      <li>
        <svg class="icon" viewBox="0 0 12 12" aria-hidden="true"><rect width="12" height="12" rx="2" fill="#7dc242"/><path d="M3.5,2.5 L5,2.5 L5.6,4.4 L4.7,5.1 C5.2,6.2 5.8,6.8 6.9,7.3 L7.6,6.4 L9.5,7 L9.5,8.5 C6,8.8 3.2,6 3.5,2.5 Z" fill="#0b0b0b"/></svg>
        (302) 555-0147
      </li>
      <li>
        <svg class="icon" viewBox="0 0 12 12" aria-hidden="true"><rect width="12" height="12" rx="2" fill="#7dc242"/><rect x="2" y="3.5" width="8" height="5.5" fill="#0b0b0b"/><path d="M2,3.5 L6,6.6 L10,3.5" fill="none" stroke="#7dc242" stroke-width="0.9"/></svg>
        info@quillorynest.com
      </li>
      <li>
        <svg class="icon" viewBox="0 0 12 12" aria-hidden="true"><circle cx="6" cy="6" r="5.5" fill="#7dc242"/><g fill="none" stroke="#0b0b0b" stroke-width="0.8"><circle cx="6" cy="6" r="4"/><ellipse cx="6" cy="6" rx="1.8" ry="4"/><path d="M2,6 H10"/></g></svg>
        www.quillorynest.com
      </li>
    </ul>
  </section>

  <section class="card card-back">
    <div class="brand brand-back"><span class="brand-dot"></span>Quillory Nest</div>
    <p class="back-url">www.quillorynest.com</p>
  </section>
</body>
</html>
```